TGV Electricial Contracting Services

Hi guys, after a design for my small electrical company, have logo design files to be incorporated into the layout, the basic concept is electrical contracting services for residential, commercial, industrial & data services, image is clean clear and strong,

Card format is to have a nice clean logo on front,with maybe the Residential – commercial – industrial - data, followed with licensed & insured, followed by contact details on backside of the card.

Target Market(s)

Residential, commercial, industrial sectors.

Industry/Entity Type

Electrical

Contact Information for Business Card

TGV logo,
Residential – commercial – industrial - data
REC: 57310
Email: tgv@wavolink.net.au
Phone: 0472 358 129

Requirements
Must have
• Clean & strong design.
Nice to have
• If possible, I would like the logo colours inverted so the text is orange and the background is black on the front of the card, then the backside of the card be the reverse colour
Should not have
• No Sparks, lightning bolts,

```html
<!DOCTYPE html>
<html lang="en">
<head>
<meta charset="utf-8">
<title>TGV Electrical – Business Card</title>
<link rel="stylesheet" href="https://fonts.googleapis.com/css2?family=Poppins:wght@600&family=Questrial&display=swap">
<style>
  :root {
    --page-bg: #d8d2cb;
    --card-bg: #000000;
    --card-edge: #9a9a9a;
    --accent: #f0892c;
    --accent-soft: #e98a34;
  }
  html, body {
    margin: 0;
    padding: 0;
    width: 1200px;
    height: 750px;
    overflow: hidden;
    background: var(--page-bg);
  }
  .canvas {
    position: relative;
    width: 1200px;
    height: 750px;
  }
  .card {
    position: absolute;
    top: 238px;
    width: 490px;
    height: 280px;
    box-sizing: border-box;
    background: var(--card-bg);
    border: 2px solid var(--card-edge);
    color: var(--accent);
    text-align: center;
    font-family: "Questrial", "Century Gothic", sans-serif;
  }
  .card--front { left: 90px; }
  .card--back { left: 623px; }

  .brand-mark {
    position: absolute;
    top: 44px;
    left: 0;
    right: 0;
    font-family: "Questrial", "Century Gothic", sans-serif;
    font-size: 84px;
    line-height: 1;
    letter-spacing: 2px;
    color: var(--accent);
  }
  .brand-name {
    position: absolute;
    top: 144px;
    left: 0;
    right: 0;
    font-family: "Poppins", "Century Gothic", sans-serif;
    font-weight: 600;
    font-size: 19px;
    line-height: 1;
    color: var(--accent);
  }
  .brand-services {
    position: absolute;
    top: 174px;
    left: 0;
    right: 0;
    font-size: 17px;
    line-height: 20px;
    color: var(--accent-soft);
  }

  .contact-name {
    position: absolute;
    top: 84px;
    left: 0;
    right: 0;
    font-family: "Poppins", "Century Gothic", sans-serif;
    font-weight: 600;
    font-size: 23px;
    line-height: 1;
  }
  .contact-list {
    position: absolute;
    top: 128px;
    left: 0;
    right: 0;
    margin: 0;
    font-size: 18px;
    line-height: 22px;
    color: var(--accent-soft);
  }
  .contact-list p { margin: 0; }
  .contact-services {
    position: absolute;
    top: 232px;
    left: 0;
    right: 0;
    margin: 0;
    font-size: 15px;
    line-height: 19px;
    color: var(--accent-soft);
  }
</style>
</head>
<body>
  <main class="canvas">
    <section class="card card--front" aria-label="Card front">
      <div class="brand-mark">TGV</div>
      <div class="brand-name">TGV Electrical</div>
      <div class="brand-services">
        Residential – commercial – industrial<br>
        data REC: 57310
      </div>
    </section>

    <section class="card card--back" aria-label="Card back">
      <div class="contact-name">Tom Vickers</div>
      <div class="contact-list">
        <p>Email:&nbsp;&nbsp; tgv@wavolink.net.au</p>
        <p>Phone: 0472 358 129</p>
      </div>
      <p class="contact-services">
        Rewiring Repairs Maintenance 24 hours Faults<br>
        and Emergency Assistance
      </p>
    </section>
  </main>
</body>
</html>
```